依頼詳細
ターゲットは20~40代の女性で『体験レッスンが無料』です。
体験レッスンの人数を増やしたいので、体験レッスンに行きたくなるようなバナーの制作をお願いいたします。
記載項目
・駅から徒歩1分
・手ぶらでOK
・無料体験レッスン実施中
サイズ
• 1200×1500と1080×1920の二種類
希望イメージ
シンプル 複雑
単色 カラフル
暗い 明るい
日常 高級
遊び心 厳粛
未来的 伝統的
女性的 男性的
希望する色
緑系
納品ファイル
• 高解像度JPG (.jpg)
• イラストレーター形式 (.ai)
補足説明
HPのURLは添付ファイルを参照ください。
■ 選んだ理由

今回の選んだ作品の気に入ったポイントは
「ルミナポストの広告バナー」として使用するという点で、一瞬流れた広告でも目が引くようなデザインと
こちらのヨガスタジオのコンセプトに合わせたハワイらしい明るくかわいらしいデザインがとても惹かれ、選出させていただきました。

■ 提案者全員のお礼・コメント

今回、たくさんの素敵なデザインのご提案
誠にありがとうございました。
どれも素敵な作品で、1つに絞るのがとても大変でした。
また、ご縁がありましたらどうぞ宜しくお願い申し上げます。
改めまして、今回ご提案してくださった皆様に心から感謝申し上げます。

```html
<!DOCTYPE html>
<html lang="ja">
<head>
<meta charset="utf-8">
<title>ヨガスタジオ Kalena 無料体験レッスン</title>
<link href="https://fonts.googleapis.com/css2?family=Noto+Serif+JP:wght@500;700;900&family=Noto+Sans+JP:wght@500;700;900&display=swap" rel="stylesheet">
<style>
:root{
  --ink:#2b2b2b;
  --charcoal:#2f2f2f;
  --band:#3a3a3a;
  --gold:#c9a66b;
  --orange:#f39a3c;
  --orange-deep:#ea7f1c;
  --brown:#7a5a3a;
  --white:#ffffff;
  --leaf:#e3ebe0;
}
*{margin:0;padding:0;box-sizing:border-box}
html,body{width:675px;height:1200px;overflow:hidden;background:var(--white)}
.banner{position:relative;width:675px;height:1200px;overflow:hidden;background:var(--white);font-family:"Noto Sans JP",sans-serif;color:var(--ink)}
.hero-photo{position:absolute;left:0;top:0;width:675px;height:472px;
  background:
    radial-gradient(ellipse 120px 260px at 120px 300px,#f7f3ee 0%,#efe6dc 60%,transparent 100%),
    radial-gradient(circle at 330px 120px,#f6d98a 0%,transparent 38%),
    radial-gradient(circle at 520px 260px,#f2b9a8 0%,transparent 35%),
    radial-gradient(circle at 600px 60px,#b9d8c4 0%,transparent 35%),
    radial-gradient(circle at 40px 60px,#d9c3a6 0%,transparent 40%),
    linear-gradient(120deg,#e8d2b8 0%,#f4e3c9 40%,#d7e4d6 70%,#f0d6c4 100%)}
.brand{position:absolute;right:60px;top:62px;font-family:"Noto Serif JP",serif;font-weight:500;font-size:40px;color:var(--white);letter-spacing:1px}
.intro{position:absolute;left:0;top:338px;width:675px;height:134px;background:rgba(255,255,255,.82)}
.intro-text{position:absolute;left:40px;top:370px;font-family:"Noto Serif JP",serif;font-weight:900;font-size:31px;line-height:46px;color:var(--ink);letter-spacing:1px}
.more-btn{position:absolute;left:558px;top:387px;width:106px;height:59px;background:var(--brown);color:var(--white);font-size:16px;font-weight:700;line-height:22px;padding:8px 0 0 10px}
.more-btn svg{position:absolute;right:8px;top:20px}
.leaves{position:absolute;left:0;top:472px;width:675px;height:603px;background:radial-gradient(circle at 90% 20%,var(--leaf),transparent 45%),radial-gradient(circle at 10% 75%,var(--leaf),transparent 40%)}
.offer-box{position:absolute;left:40px;top:513px;width:365px;height:286px;background:var(--charcoal);border:3px solid var(--gold);outline:2px solid var(--gold);outline-offset:-12px}
.offer-text{position:absolute;left:62px;top:533px;font-family:"Noto Serif JP",serif;font-weight:500;font-size:58px;line-height:78px;color:var(--white);letter-spacing:6px}
.badge{position:absolute;width:166px;height:166px;border-radius:50%;background:var(--orange);color:var(--white);text-align:center;display:flex;flex-direction:column;justify-content:center;align-items:center}
.badge-title{font-family:"Noto Serif JP",serif;font-weight:700;font-size:34px;line-height:44px}
.badge-sub{font-size:19px;font-weight:700;line-height:25px}
.badge-station{left:468px;top:507px}
.badge-hands{left:468px;top:690px}
.scene{position:absolute;top:878px;height:180px}
.scene-pair{left:67px;width:270px;background:linear-gradient(180deg,#f4f2ee,#d8d2c8)}
.scene-pose{left:360px;width:248px;background:linear-gradient(180deg,#d9c6a8,#e9c76d)}
.price-band{position:absolute;left:0;top:1075px;width:675px;height:125px;background:var(--band);color:var(--white)}
.price-lead{position:absolute;left:20px;top:26px;width:28px;font-size:24px;font-weight:700;line-height:28px}
.price-num{position:absolute;left:58px;top:22px;font-family:"Noto Serif JP",serif;font-size:64px;font-weight:700;line-height:76px}
.price-unit{position:absolute;left:252px;top:32px;font-size:24px;font-weight:700;line-height:30px}
.price-note{position:absolute;left:248px;top:68px;font-size:18px;font-weight:700;line-height:26px}
.price-arrow{position:absolute;left:338px;top:44px}
.now-free{position:absolute;left:378px;top:28px;width:128px;height:70px;background:var(--orange-deep);text-align:center;font-size:24px;font-weight:900;line-height:32px;padding-top:3px}
.zero{position:absolute;left:518px;top:0;font-family:"Noto Serif JP",serif;font-size:110px;font-weight:900;line-height:125px;color:var(--orange)}
.zero-unit{position:absolute;left:598px;top:62px;font-size:38px;font-weight:900;color:var(--orange)}
</style>
</head>
<body>
<div class="banner">
  <div class="hero-photo" role="img" aria-label="明るい壁画の前でヨガのポーズをとる女性インストラクターの写真"></div>
  <div class="brand">Kalena</div>
  <div class="intro"></div>
  <p class="intro-text">恵比寿駅から徒歩1分！<br>ヨガスタジオ「Kalena」</p>
  <div class="more-btn">詳しくは<br>コチラ
    <svg width="20" height="18" viewBox="0 0 20 18"><path d="M2 2l7 7-7 7M10 2l7 7-7 7" fill="none" stroke="#fff" stroke-width="2.5"/></svg>
  </div>
  <div class="leaves" role="img" aria-label="淡いヤシの葉の背景"></div>
  <div class="offer-box"></div>
  <p class="offer-text">無料体験<br>レッスン<br>実施中！</p>
  <div class="badge badge-station"><span class="badge-title">駅近</span><span class="badge-sub">駅から<br>徒歩1分</span></div>
  <div class="badge badge-hands"><span class="badge-title">手ぶら</span><span class="badge-sub">用意は<br>いらない</span></div>
  <div class="scene scene-pair" role="img" aria-label="スタジオでポーズをとる二人の女性の写真"></div>
  <div class="scene scene-pose" role="img" aria-label="ヨガマットの上で座って瞑想する女性の写真"></div>
  <div class="price-band">
    <p class="price-lead">通常</p>
    <p class="price-num">2,000</p>
    <p class="price-unit">円</p>
    <p class="price-note">のところ</p>
    <svg class="price-arrow" width="20" height="34" viewBox="0 0 20 34"><path d="M2 2l16 15L2 32z" fill="#fff"/></svg>
    <div class="now-free">今だけ<br>無料</div>
    <p class="zero">0</p>
    <p class="zero-unit">円</p>
  </div>
</div>
</body>
</html>
```